Custom CV (resume) Template in Word 2013

We are a boutique Marketing Agency that specialises in outsourcing our staff to work with clients internally. As such it is imperitive that we are able to communicate the capabilities and experience of our staff to our clients in a simple, succinct, and engaging manner. In this endeavour we look to commission a CV (resume) template that utilises our intellectual property, logo, and corporate colours to be used for existing and future staff in order to better market them to clients.
Our firm places a high value on being a ‘one-page’ business. As such we would strongly prefer that all submissions are limited to a single sheet. Designs must include the following components:
•	Place for Candidates Name
•	Place for our logo (logo is attached)
•	Place for our contact information
•	A section for an introduction or blurb about the candidate
•	A table (or similar) for listing previous experience and a summary of each experience
•	A table (or similar) where candidates can list the relevant industries in which they have experience
The following are our brand colours:
•	C: 56 M:0 Y:100 K:27        R:94 G:151 B:50
•	C:0 M:10 Y:33 K:72           R:105 G:94 B:74
•	C:0 M:8 Y:26 K:57              R:135 G:124 B:105
This template must be delivered in Word 2010 or 2013. As long as the parameters above are met we are flexible to the design elements.
I have also attached an example from one of our competitors and have removed their details for their privacy as an example of something we are looking for.

```html
<!DOCTYPE html>
<html lang="en">
<head>
<meta charset="utf-8">
<title>Candidate CV – Canopy Crew</title>
<link rel="stylesheet" href="https://fonts.googleapis.com/css2?family=Overpass:ital,wght@0,300;0,400;0,700;1,300&family=Archivo+Narrow:wght@400&display=swap">
<style>
  :root {
    --brand-green: #5e9732;
    --brand-brown: #695e4a;
    --brand-taupe: #877c69;
    --panel-sand: #ddd5c3;
    --paper: #ffffff;
    --rule: #d8d8d8;
    --footer-text: #6b6152;
    --leaf-dark: #1f6b3a;
    --leaf-light: #d9dcc9;
  }
  * { box-sizing: border-box; margin: 0; padding: 0; }
  html, body { width: 850px; height: 1200px; overflow: hidden; background: var(--paper); }
  .cv-page {
    position: relative;
    width: 850px;
    height: 1200px;
    background: var(--paper);
    font-family: "Overpass", Arial, sans-serif;
    overflow: hidden;
  }

  /* Decorative artwork placeholders */
  .foliage-art {
    position: absolute;
    left: 0; top: 0;
    width: 330px; height: 440px;
    background: radial-gradient(ellipse at 0% 0%, var(--leaf-dark) 0%, rgba(94,151,50,0.55) 35%, rgba(217,220,201,0.45) 60%, rgba(255,255,255,0) 78%);
  }
  .mascot-art {
    position: absolute;
    left: 64px; top: 6px;
    width: 146px; height: 212px;
    border-radius: 60px 60px 18px 18px;
    background: linear-gradient(180deg, #8a7a56 0%, #c9c08f 45%, #a49a6c 100%);
  }

  /* Header band */
  .name-band {
    position: absolute;
    left: 222px; top: 25px;
    width: 628px; height: 172px;
    background: var(--brand-brown);
    border-radius: 22px 0 0 22px;
    color: var(--paper);
    padding: 26px 0 0 40px;
  }
  .candidate-name {
    font-weight: 400;
    font-size: 47px;
    letter-spacing: 1.5px;
    line-height: 60px;
  }
  .candidate-role {
    margin-top: 12px;
    font-weight: 300;
    font-style: italic;
    font-size: 24px;
    letter-spacing: 1px;
  }

  /* Content panels */
  .panel {
    position: absolute;
    border-radius: 46px;
  }
  .panel-title {
    font-family: "Overpass", Arial, sans-serif;
    font-weight: 300;
    font-size: 25px;
    letter-spacing: 0.5px;
    line-height: 30px;
  }
  .experience-panel {
    left: 47px; top: 216px;
    width: 756px; height: 491px;
    background: var(--panel-sand);
    border: 1px solid var(--brand-taupe);
    border-radius: 70px;
    padding: 22px 56px 0 36px;
    color: var(--brand-brown);
  }
  .experience-panel .panel-title { color: var(--brand-brown); margin-bottom: 2px; }
  .experience-text {
    font-size: 17.4px;
    line-height: 25.4px;
    text-align: justify;
    color: var(--brand-taupe);
    letter-spacing: 0.6px;
  }
  .experience-text + .experience-text { margin-top: 13px; }

  .industry-panel {
    left: 48px; top: 732px;
    width: 367px; height: 358px;
    background: var(--brand-green);
    padding: 26px 12px 0 37px;
    color: var(--paper);
  }
  .clients-panel {
    left: 434px; top: 732px;
    width: 369px; height: 358px;
    background: var(--panel-sand);
    border: 1px solid var(--brand-taupe);
    padding: 25px 30px 0 32px;
    color: var(--brand-taupe);
  }
  .clients-panel .panel-title { color: var(--brand-brown); }
  .panel-note {
    margin-top: 14px;
    font-family: "Archivo Narrow", "Arial Narrow", sans-serif;
    font-size: 17.5px;
    line-height: 26.4px;
    text-align: justify;
  }

  /* Footer */
  .footer-rule {
    position: absolute;
    left: 0; top: 1092px;
    width: 800px; height: 1px;
    background: var(--rule);
  }
  .contact-block {
    position: absolute;
    left: 46px; top: 1106px;
    font-size: 13.6px;
    line-height: 18.6px;
    color: var(--footer-text);
    letter-spacing: 0.3px;
    font-style: normal;
  }
  .brand-mark {
    position: absolute;
    left: 540px; top: 1112px;
    display: flex;
    align-items: center;
    gap: 10px;
  }
  .brand-dot {
    width: 18px; height: 18px;
    border-radius: 50%;
    background: var(--brand-green);
  }
  .brand-name {
    font-family: "Overpass", Arial, sans-serif;
    font-weight: 700;
    font-size: 36px;
    line-height: 44px;
    color: var(--brand-green);
    letter-spacing: -0.5px;
  }
</style>
</head>
<body>
<main class="cv-page">
  <div class="foliage-art" role="img" aria-label="Tropical jungle leaves illustration"></div>
  <div class="mascot-art" role="img" aria-label="Illustrated safari explorer mascot holding binoculars"></div>

  <header class="name-band">
    <h1 class="candidate-name">CANDIDATE NAME</h1>
    <p class="candidate-role">DESIGNATION / ROLE</p>
  </header>

  <section class="panel experience-panel">
    <h2 class="panel-title">WORK EXPERIENCE</h2>
    <p class="experience-text">Lorem ipsum dolor sit amet, consectetuer adipiscing elit, sed diam nonummy nibh euismod tincidunt ut laoreet dolore magna aliquam erat volutpat. Ut wisi enim ad minim veniam, quis nostrud exerci tation ullamcorper suscipit lobortis nisl ut aliquip ex ea commodo consequat. Duis autem vel eum iriure dolor in hendrerit in vulputate velit esse molestie consequat, vel illum dolore eu feugiat nulla facilisis at vero eros et accumsan et iusto odio dignissim qui blandit praesent luptatum zzril delenit augue duis dolore te feugait nulla facilisi. Nam liber tempor cum soluta nobis eleifend option congue nihil imperdiet doming id quod mazim placerat facer possim assum.</p>
    <p class="experience-text">Lorem ipsum dolor sit amet, consectetuer adipiscing elit, sed diam nonummy nibh euismod tincidunt ut laoreet dolore magna aliquam erat volutpat. Ut wisi enim ad minim veniam, quis nostrud exerci tation ullamcorper suscipit lobortis nisl ut aliquip ex ea commodo consequat.</p>
  </section>

  <section class="panel industry-panel">
    <h2 class="panel-title">INDUSTRY</h2>
    <p class="panel-note">[Type a quote from the document or the summary of an interesting point. You can position the text box anywhere in the document. Use the Text Box Tools tab to change the formatting of the pull quote text box.]</p>
  </section>

  <section class="panel clients-panel">
    <h2 class="panel-title">CLIENTS</h2>
    <p class="panel-note">[Type a quote from the document or the summary of an interesting point. You can position the text box anywhere in the document. Use the Text Box Tools tab to change the formatting of the pull quote text box.]</p>
  </section>

  <div class="footer-rule"></div>
  <address class="contact-block">
    48 Fernleaf Road, Riverton Qld 4100<br>
    P.O. Box 2207, Fernleaf Road Riverton Qld 4100<br>
    Contact 1300 00 CREW (2739) | 07 5550 1842 | hello@canopycrew.com.au<br>
    www.canopycrew.com.au
  </address>
  <div class="brand-mark">
    <span class="brand-dot"></span>
    <span class="brand-name">Canopy Crew</span>
  </div>
</main>
</body>
</html>
```